Online video and marketing company business cards

Need to get some new business cards designed to fit with our new logo. The cards should be professional, clean and simple.

Cards should have:

Name
Position
2 line address
telephone
mobile
email address
web address

We need to have our logo and if possible say what we do...
ONLINE FILM PRODUCTION & STRATEGY

Industry/Entity Type

Marketing

```html
<!DOCTYPE html>
<html lang="en">
<head>
<meta charset="utf-8">
<title>pinreeltv business cards</title>
<link href="https://fonts.googleapis.com/css2?family=Source+Sans+3:wght@400;600;700&display=swap" rel="stylesheet">
<style>
  :root {
    --navy: #1d4f7e;
    --sky: #6ea6cc;
    --ink: #4a4f55;
    --muted: #6b7077;
    --card: #f7f7f6;
    --backdrop: #e6e4e0;
  }
  * { box-sizing: border-box; margin: 0; padding: 0; }
  html, body { width: 1200px; height: 720px; overflow: hidden; }
  body {
    background: var(--backdrop);
    font-family: "Source Sans 3", "Myriad Pro", sans-serif;
    position: relative;
  }
  .card {
    position: absolute;
    top: 205px;
    width: 540px;
    height: 310px;
    background: var(--card);
    border-radius: 4px;
    box-shadow: 0 6px 18px rgba(0,0,0,0.18);
    overflow: hidden;
  }
  .card--details { left: 40px; }
  .card--brand { left: 620px; }

  /* details side */
  .brand-mark {
    position: absolute;
    left: 34px;
    top: 34px;
    display: flex;
    align-items: center;
    gap: 12px;
  }
  .brand-mark__dot {
    width: 40px; height: 40px;
    border-radius: 50%;
    border: 6px solid var(--navy);
  }
  .brand-mark__name {
    font-size: 50px;
    font-weight: 700;
    color: var(--navy);
    letter-spacing: -1px;
    line-height: 1;
  }
  .person {
    position: absolute;
    right: 28px;
    top: 108px;
    text-align: right;
  }
  .person__name {
    font-size: 19px;
    font-weight: 700;
    color: var(--navy);
    line-height: 1.1;
  }
  .person__title {
    font-size: 14px;
    color: var(--muted);
  }
  .edge-tab {
    position: absolute;
    right: -8px;
    top: 104px;
    width: 16px;
    height: 44px;
    border-radius: 8px;
    background: var(--sky);
  }
  .edge-bar {
    position: absolute;
    left: -8px;
    top: 170px;
    width: 18px;
    height: 118px;
    border-radius: 9px;
    background: var(--navy);
  }
  .contact {
    position: absolute;
    left: 30px;
    top: 168px;
    list-style: none;
    font-size: 14.5px;
    color: var(--ink);
    line-height: 21px;
  }
  .contact li { display: flex; align-items: center; gap: 8px; }
  .contact svg { width: 13px; height: 13px; flex: none; }
  .contact .address { padding-left: 0; }

  /* brand side */
  .brand-feature {
    position: absolute;
    left: 0; right: 0;
    top: 70px;
    display: flex;
    justify-content: center;
    align-items: center;
    gap: 16px;
  }
  .brand-feature__dot {
    width: 56px; height: 56px;
    border-radius: 50%;
    border: 9px solid var(--navy);
  }
  .brand-feature__name {
    font-size: 64px;
    font-weight: 700;
    color: var(--navy);
    letter-spacing: -1.5px;
    line-height: 1;
  }
  .tagline {
    position: absolute;
    left: 0; right: 0;
    top: 206px;
    text-align: center;
    font-size: 17px;
    font-weight: 600;
    letter-spacing: 2.2px;
    color: var(--navy);
  }
  .web {
    position: absolute;
    left: 0; right: 0;
    top: 240px;
    text-align: center;
    font-size: 17px;
    letter-spacing: 4px;
    color: var(--ink);
  }
</style>
</head>
<body>
  <section class="card card--details" aria-label="Business card, contact side">
    <div class="brand-mark">
      <span class="brand-mark__dot"></span>
      <span class="brand-mark__name">pinreeltv</span>
    </div>

    <span class="edge-tab"></span>
    <div class="person">
      <p class="person__name">Your Name</p>
      <p class="person__title">Title</p>
    </div>

    <span class="edge-bar"></span>
    <ul class="contact">
      <li>
        <svg viewBox="0 0 16 16"><circle cx="8" cy="8" r="8" fill="var(--navy)"/><path d="M5 4.5l1.6-.4.9 2-1 .8a5 5 0 0 0 2.6 2.6l.8-1 2 .9-.4 1.6c-3.6.2-6.7-2.9-6.5-6.5z" fill="#fff"/></svg>
        123-456-0789
      </li>
      <li>
        <svg viewBox="0 0 16 16"><rect x="3.5" y="1" width="9" height="14" rx="1.5" fill="var(--navy)"/><rect x="5" y="3" width="6" height="7" fill="#fff"/><rect x="5" y="11.5" width="6" height="2" fill="#fff"/></svg>
        123-456-0789
      </li>
      <li>
        <svg viewBox="0 0 16 16"><circle cx="8" cy="8" r="8" fill="var(--navy)"/><rect x="3.5" y="5" width="9" height="6.5" fill="#fff"/><path d="M3.5 5L8 8.6 12.5 5" stroke="var(--navy)" fill="none"/></svg>
        info@pinreeltv.com
      </li>
      <li>
        <svg viewBox="0 0 16 16"><circle cx="8" cy="8" r="8" fill="var(--navy)"/><circle cx="8" cy="8" r="4.5" fill="none" stroke="#fff"/><path d="M3.5 8h9M8 3.5c-2 2.5-2 6.5 0 9M8 3.5c2 2.5 2 6.5 0 9" stroke="#fff" fill="none"/></svg>
        www.pinreeltv.com
      </li>
      <li class="address">Street Name, City Name</li>
      <li class="address">State Zip Code</li>
    </ul>
  </section>

  <section class="card card--brand" aria-label="Business card, brand side">
    <div class="brand-feature">
      <span class="brand-feature__dot"></span>
      <span class="brand-feature__name">pinreeltv</span>
    </div>
    <p class="tagline">ONLINE FILM PRODUCTION &amp; STRATEGY</p>
    <p class="web">www.pinreeltv.com</p>
  </section>
</body>
</html>
```